Services Brochure

We need an revised brochure for our 3 main services. I have uploaded our old Brochure for reference. We have 3 main services (Managed IT Services, Business VoIP, Business Internet). Below is some text we would like included in the brochure for each service section. In addition I have attached a "mock up" showing that we want IT Services on top, VoIP in the middle and Internet at the bottom. Please use your design experience to select images that would fit well. I also included an image of the phone we would like to use.
Text for Brochure:
Title/Header: Unleash the Power of Local IT Solutions
IT Services That Mean Business
Experience fanatical customer service with our affordable, full-service IT solutions. We’re 100% local, ensuring leading response times and personalized support—so you can focus on what you do best.
Talk More, Worry Less with Our Telephone Services
Say goodbye to overpriced equipment and hello to our free phone plan. Keep your number and enjoy unlimited local and long-distance calling. Tailor your phone system to your business needs and rest assured—our rates are always the lowest in town.
Highspeed Internet That Sets You Apart
Stay connected with blazing-fast speeds—from 1Gbps to 10Gbps, both up and down. Benefit from a static IP address and unbeatable prices, backed by 100% local support. Get the connectivity your business deserves at the best value in town.
Elevate your business with cutting-edge technology.
Sorry everyone the banner size is 81" high and 33" wide.

```html
<!DOCTYPE html>
<html lang="en">
<head>
<meta charset="utf-8">
<title>Norvale – Local IT Solutions Banner</title>
<link href="https://fonts.googleapis.com/css2?family=Montserrat:wght@400;600;700&family=Bebas+Neue&display=swap" rel="stylesheet">
<style>
  :root {
    --stage: #8e8e8e;
    --navy: #0c1150;
    --navy-deep: #080b3a;
    --royal: #1a2a9c;
    --green: #8dc63f;
    --ink: #1d1d24;
    --light: #e3e3e3;
    --white: #ffffff;
  }
  * { box-sizing: border-box; margin: 0; padding: 0; }
  html, body { width: 912px; height: 1200px; overflow: hidden; }
  body {
    position: relative;
    background: var(--stage);
    font-family: "Montserrat", sans-serif;
    color: var(--ink);
  }
  /* 33 × 81 tall banner */
  .banner {
    position: absolute; left: 212px; top: 0;
    width: 489px; height: 1200px;
    background: var(--light);
    overflow: hidden;
  }
  .hero {
    position: absolute; left: 0; top: 0; width: 489px; height: 540px;
    background: radial-gradient(ellipse at 60% 55%, #17228a 0%, var(--navy) 55%, var(--navy-deep) 100%);
  }
  .brand {
    position: absolute; left: 28px; top: 26px;
    font-weight: 700; font-size: 44px; line-height: 50px;
    letter-spacing: -1.5px; color: var(--white);
  }
  .headline {
    position: absolute; left: 28px; top: 104px;
    color: var(--white); font-weight: 400; font-size: 31px; line-height: 33px;
  }
  .headline-accent {
    position: absolute; left: 27px; top: 170px;
    font-family: "Bebas Neue", sans-serif; color: var(--green);
    font-size: 82px; line-height: 82px; letter-spacing: 0.5px;
  }
  .product-photo {
    position: absolute; left: 40px; top: 268px; width: 409px; height: 182px;
    border-radius: 8px;
    background: linear-gradient(135deg, #3a3f4c 0%, #22252e 60%, #15171d 100%);
  }
  .photo-frame {
    position: absolute; left: 20px; top: 470px; width: 152px; height: 660px;
    background: var(--white);
    box-shadow: 0 2px 8px rgba(0,0,0,0.14);
  }
  .photo { position: absolute; left: 29px; width: 134px; }
  .photo--office  { top: 480px; height: 212px; background: linear-gradient(160deg, #9fb7c9 0%, #dfe6ec 55%, #6f8aa8 100%); }
  .photo--support { top: 704px; height: 210px; background: linear-gradient(160deg, #1c3a5a 0%, #0e1d30 55%, #c9c2c8 100%); }
  .photo--laptop  { top: 926px; height: 194px; background: linear-gradient(160deg, #b8aca4 0%, #8b7f78 55%, #4d4a4c 100%); }
  .service {
    position: absolute; left: 172px; width: 317px; padding: 0 14px 0 18px;
  }
  .service--it    { top: 470px; height: 230px; background: var(--green); color: var(--white); padding-top: 20px; }
  .service--voice { top: 714px; }
  .service--net   { top: 930px; }
  .service-title {
    font-weight: 700; font-size: 17px; line-height: 21px; margin-bottom: 10px;
  }
  .benefits { list-style: none; }
  .benefit {
    position: relative; padding-left: 18px; margin-bottom: 6px;
    font-size: 10.5px; line-height: 14px; font-weight: 400;
  }
  .benefit svg { position: absolute; left: 0; top: 2px; width: 12px; height: 12px; }
  .service--it .benefit svg { color: var(--white); }
  .service--voice .benefit svg,
  .service--net .benefit svg { color: var(--green); }
  .footer {
    position: absolute; left: 0; top: 1142px; width: 489px; height: 58px;
    background: var(--royal); color: var(--white);
    display: flex; align-items: center; justify-content: space-between;
    padding: 0 18px 0 24px;
  }
  .cta { font-weight: 700; font-size: 17px; letter-spacing: 0.2px; }
  .web { font-weight: 600; font-size: 11.5px; }
</style>
</head>
<body>
  <svg width="0" height="0" style="position:absolute">
    <symbol id="tick" viewBox="0 0 20 20">
      <path d="M17 7.5A8 8 0 1 1 13.5 3" fill="none" stroke="currentColor" stroke-width="1.8" stroke-linecap="round"/>
      <path d="M6 10l3 3 8-8" fill="none" stroke="currentColor" stroke-width="2" stroke-linecap="round" stroke-linejoin="round"/>
    </symbol>
  </svg>

  <main class="banner">
    <header class="hero">
      <div class="brand">norvale</div>
      <h1 class="headline">Unleash the<br>Power of Local</h1>
      <div class="headline-accent">IT SOLUTIONS</div>
      <div class="product-photo" role="img" aria-label="Photo of a dark grey desk IP phone with colour screen and coiled handset"></div>
    </header>

    <div class="photo-frame"></div>
    <div class="photo photo--office" role="img" aria-label="Photo of smiling staff on headsets at desks in a bright office"></div>
    <div class="photo photo--support" role="img" aria-label="Photo of a support agent with a headset in a server room"></div>
    <div class="photo photo--laptop" role="img" aria-label="Photo of hands typing on a laptop with a Wi-Fi symbol overlay"></div>

    <section class="service service--it">
      <h2 class="service-title">IT Services That<br>Mean Business</h2>
      <ul class="benefits">
        <li class="benefit"><svg><use href="#tick"/></svg>Experience fanatical customer service with our affordable, full-service IT solutions</li>
        <li class="benefit"><svg><use href="#tick"/></svg>We’re 100% local, ensuring leading response times and personalized support so you can focus on what you do best</li>
      </ul>
    </section>

    <section class="service service--voice">
      <h2 class="service-title">Talk More, Worry Less with<br>Our Telephone Services</h2>
      <ul class="benefits">
        <li class="benefit"><svg><use href="#tick"/></svg>Say goodbye to overpriced equipment and hello to our free phone plan</li>
        <li class="benefit"><svg><use href="#tick"/></svg>Keep your number and enjoy unlimited local and long-distance calling</li>
        <li class="benefit"><svg><use href="#tick"/></svg>Tailor your phone system to your business needs and rest assured our rates are always the lowest in town.</li>
      </ul>
    </section>

    <section class="service service--net">
      <h2 class="service-title">Highspeed Internet That<br>Sets You Apart</h2>
      <ul class="benefits">
        <li class="benefit"><svg><use href="#tick"/></svg>Stay connected with blazing-fast speeds from 1Gbps to 10Gbps, both up and down</li>
        <li class="benefit"><svg><use href="#tick"/></svg>Benefit from a static IP address and unbeatable prices, backed by 100% local support</li>
        <li class="benefit"><svg><use href="#tick"/></svg>Get the connectivity your business deserves at the best value in town.</li>
      </ul>
    </section>

    <footer class="footer">
      <div class="cta">CALL NOW 555-014-2286</div>
      <div class="web">www.norvaletech.com</div>
    </footer>
  </main>
</body>
</html>
```